Walt's 85th Birthday Invitation

Invitation to celebrate Walt's turning 85. OKTOBERFEST with fall colors & maybe some beer steins/autumn leaves/happy/fun images. Below are my thoughts for the wording but I need someone to bring it to life.
It's not just a party
it's an
OKTOBERFEST
to celebrate
Picture of Walt
Walt's 85th birthday

Saturday, October 25, 2014

at the Lindmoor Ale Court
Pelorvale
4127 Denbury Ave.
Garden Grove, CA 92871

Cocktails at 6 Dinner at 7
Dancing & Partying till 10:00

No birthday gifts please.
Please consider a gift to PelorVale!
Casual Attire

I would like this on a horizontal 5x7 flat card that will fit the envelopes you have. The text & spacing can be adjusted. This is just a rough draft. Thank you for your help! I will need 150 invitations with envelopes.

OktoberFest

```html
<!DOCTYPE html>
<html lang="en">
<head>
<meta charset="utf-8">
<title>Walt's 85th Birthday – OktoberFest Invitation</title>
<link href="https://fonts.googleapis.com/css2?family=Open+Sans:ital,wght@0,400;0,700;0,800;1,400&family=Yellowtail&display=swap" rel="stylesheet">
<style>
  :root {
    --magenta: #d42c6e;
    --magenta-soft: #e47aa3;
    --blush: #fbe3e5;
    --blush-deep: #f6d3d9;
    --ink: #2b2b2b;
    --white: #ffffff;
  }
  * { margin: 0; padding: 0; box-sizing: border-box; }
  html, body { width: 1200px; height: 857px; overflow: hidden; background: var(--blush); }
  .invitation {
    position: relative;
    width: 1200px;
    height: 857px;
    background: var(--blush);
    font-family: "Open Sans", Arial, sans-serif;
    color: var(--ink);
    overflow: hidden;
  }
  .side-band {
    position: absolute;
    left: 0; top: 0;
    width: 385px; height: 857px;
    background: linear-gradient(to bottom, var(--magenta) 0%, var(--magenta) 58%, var(--magenta-soft) 80%, var(--blush-deep) 100%);
  }
  .flourish {
    position: absolute;
    left: 0; top: 153px;
    width: 218px; height: 382px;
    border-radius: 0 60% 45% 0 / 0 50% 40% 0;
    background: radial-gradient(ellipse at 30% 45%, rgba(255,255,255,0.55), rgba(255,255,255,0.15) 70%, rgba(255,255,255,0) 100%);
  }
  .badge {
    position: absolute;
    left: 38px; top: 562px;
    width: 306px; height: 306px;
  }
  .badge-curve {
    font-family: "Open Sans", Arial, sans-serif;
    font-weight: 700;
    font-size: 19px;
    letter-spacing: 2px;
    fill: var(--white);
  }
  .badge-number {
    font-family: "Open Sans", Arial, sans-serif;
    font-weight: 700;
    font-size: 86px;
    fill: var(--white);
  }
  .title {
    position: absolute;
    left: 510px; top: 22px;
    white-space: nowrap;
    line-height: 1;
  }
  .title-script {
    font-family: "Yellowtail", cursive;
    font-size: 92px;
    color: var(--magenta);
  }
  .title-bold {
    font-weight: 800;
    font-size: 86px;
    color: var(--ink);
    letter-spacing: -1px;
  }
  .copy {
    position: absolute;
    left: 428px;
    font-size: 25px;
    line-height: 35px;
    white-space: nowrap;
  }
  .lead { top: 193px; }
  .lead-highlight {
    color: var(--magenta);
    font-size: 34px;
    margin-left: 14px;
    vertical-align: -2px;
  }
  .occasion { top: 275px; }
  .date { top: 352px; font-weight: 700; }
  .venue { top: 420px; line-height: 34px; }
  .schedule { top: 591px; font-style: italic; }
  .notes { top: 696px; line-height: 33px; }
  .big-age {
    position: absolute;
    left: 800px; top: 416px;
    font-weight: 700;
    font-size: 340px;
    line-height: 1;
    letter-spacing: -14px;
    color: var(--white);
    text-shadow: -9px 9px 12px rgba(0,0,0,0.55);
    white-space: nowrap;
  }
</style>
</head>
<body>
<main class="invitation">
  <div class="side-band"></div>
  <div class="flourish" role="img" aria-label="White decorative swirl ornament"></div>

  <svg class="badge" viewBox="0 0 338 338" xmlns="http://www.w3.org/2000/svg">
    <defs>
      <path id="arc-top" d="M 44 169 A 125 125 0 0 1 294 169"/>
      <path id="arc-bottom" d="M 36 175 A 133 133 0 0 0 302 175"/>
    </defs>
    <circle cx="169" cy="169" r="168" fill="var(--magenta)"/>
    <circle cx="169" cy="169" r="112" fill="none" stroke="var(--white)" stroke-width="4"/>
    <circle class="badge-leaf" cx="169" cy="172" r="98" fill="var(--white)" opacity="0.35" role="img" aria-label="Autumn maple leaf emblem"/>
    <text class="badge-curve"><textPath href="#arc-top" startOffset="50%" text-anchor="middle">CELEBRATING 85 YEARS</textPath></text>
    <text class="badge-curve"><textPath href="#arc-bottom" startOffset="50%" text-anchor="middle">WALT’S  BIRTHDAY</textPath></text>
    <text class="badge-number" x="169" y="200" text-anchor="middle">85</text>
  </svg>

  <h1 class="title"><span class="title-script">Oktober</span><span class="title-bold">Fest</span></h1>

  <p class="copy lead">It's not just a party……. <span class="lead-highlight">it’s an OKTOBERFEST</span></p>
  <p class="copy occasion">to celebrate, Picture of Walt Walt’s 85th birthday</p>
  <p class="copy date">Saturday, October 25, 2014</p>
  <p class="copy venue">at the Lindmoor Ale Court<br>Pelorvale<br>4127 Denbury Ave.<br>Garden Grove, CA 92871</p>
  <p class="copy schedule">Cocktails at 6 Dinner at 7<br>Dancing &amp; Partying till 10:00</p>
  <p class="copy notes">No birthday gifts please.<br>Please consider a gift to PelorVale!<br>Casual Attire</p>

  <div class="big-age" aria-hidden="true">85</div>
</main>
</body>
</html>
```